Consumer Protection Law Firm Needs a New Website

We need a new website for our law firm. We practice consumer protection law, with an emphasis on class actions. In particular, we serve consumers who are harassed by telemarketers, debt collectors, abusive companies, and financial criminals. In short, we sue big companies that do bad things to lots of people.

The lawyer is Carl Wendrow. Current website is available through www.WendrowLaw.example. Some logo files are attached.

Prefer designs that use the colors black, red, and white, per the logo. Also prefer clean, lightweight HTML5/CSS3 design rather than Wordpress. Finally, single-page type design preferred over multi-page, but flexible.

I have some limited familiarity with HTML and CSS, particularly Bootstrap, so a Bootstrap type design that I can modify myself would be ideal.

Target Market(s)

Consumers with cellular telephones.

Industry/Entity Type

Law Firm

Coding

Coded - Design and coding required

Number of Pages Required

1 page

Requirements
Must have
• - Mobile friendly, preferably without requiring separate design. In other words, a framework like Bootstrap is preferred.
• - Contact Form
• - A section for recent results
• - A section for a picture and bio of Carl Wendrow, Esq.
Nice to have
• - Animated elements that count-up and populate with numbers for things like:
• * X dollars recovered for consumers.
• * Y clients represented
• * Over Z lawsuits filed for consumers

```html
<!DOCTYPE html>
<html lang="en">
<head>
<meta charset="utf-8">
<title>Wendrow Law – Consumer Advocates</title>
<link href="https://fonts.googleapis.com/css2?family=Open+Sans:wght@400;600;700;800&display=swap" rel="stylesheet">
<style>
:root{
  --red:#b3103d;
  --red-dark:#8f0b30;
  --black:#000;
  --ink:#222;
  --text:#555;
  --grey-band:#ececec;
  --card:#e3e3e3;
  --stats-bg:#141414;
  --footer-bg:#0b0b0b;
  --footer-text:#8a8a8a;
  --white:#fff;
}
*{box-sizing:border-box;margin:0;padding:0}
html,body{width:1200px;height:2258px;overflow:hidden}
body{font-family:'Open Sans',sans-serif;color:var(--text);background:var(--white);position:relative}

/* header */
.site-header{position:absolute;left:0;top:0;width:1200px;height:90px;background:var(--white)}
.brand{position:absolute;left:108px;top:24px;display:flex;align-items:center;gap:12px}
.brand-square{width:36px;height:36px;background:var(--red)}
.brand-name{font-size:30px;font-weight:700;color:var(--ink);letter-spacing:1px;line-height:1}
.call-btn{position:absolute;left:916px;top:24px;width:165px;height:41px;background:var(--black);color:var(--white);display:flex;align-items:center;justify-content:center;gap:8px;font-size:14px}
.call-btn b{font-weight:700}

/* hero */
.hero{position:absolute;left:0;top:90px;width:1200px;height:433px;background:linear-gradient(90deg,#5a3e2e 0%,#8a6a52 30%,#6b4e3a 55%,#3d2a22 100%)}
.hero-photo{position:absolute;left:0;top:0;width:1200px;height:433px;background:radial-gradient(ellipse at 30% 55%,#c9a58a 0%,#8a6450 35%,rgba(70,45,35,0) 65%)}
.main-nav{position:absolute;left:99px;top:90px;width:1002px;height:41px;background:var(--black);display:flex;align-items:stretch}
.main-nav a{color:var(--white);text-decoration:none;font-size:14px;padding:0 16px;display:flex;align-items:center}
.main-nav a.active{background:var(--red)}
.nav-search{position:absolute;right:0;top:0;width:41px;height:41px;background:var(--red);display:flex;align-items:center;justify-content:center}
.slider-dots{position:absolute;left:150px;top:480px;display:flex;gap:8px}
.slider-dots span{width:8px;height:8px;border-radius:50%;background:rgba(255,255,255,.5)}
.consult-card{position:absolute;left:697px;top:152px;width:389px;height:340px;background:rgba(255,255,255,.93);padding:16px 24px}
.consult-card h2{color:var(--red);font-size:22.5px;font-weight:400;line-height:1.25;letter-spacing:-.2px}
.consult-card p.lead{font-size:12.5px;line-height:1.3;color:#444;margin-top:8px;text-align:justify}
.field{background:var(--white);border:1px solid #e4e4e4;height:37px;font-size:13px;color:#999;display:flex;align-items:center;padding-left:14px}
.field-row{display:flex;gap:3px;margin-top:3px}
.field-row .field{flex:1}
.consult-form{margin-top:12px}
.consult-btn{margin-top:6px;height:37px;background:var(--red);color:var(--white);font-size:14px;display:flex;align-items:center;justify-content:center}
.consult-card .note{font-size:9px;color:#333;text-align:center;margin-top:12px;white-space:nowrap}

/* section titles */
.section-title{position:absolute;left:0;width:1200px;text-align:center;font-size:30px;font-weight:700;color:var(--ink)}
.section-title .hl{color:var(--red)}
.title-rule{position:absolute;left:540px;width:120px;height:18px}
.title-rule::before{content:"";position:absolute;left:0;right:0;top:9px;border-top:1px solid #bbb}
.title-rule::after{content:"";position:absolute;left:51px;top:0;width:18px;height:18px;background:var(--red);border:3px solid var(--white)}

.btn-red{position:absolute;background:var(--red);color:var(--white);font-size:10px;font-weight:700;display:flex;align-items:center;justify-content:center;letter-spacing:.3px}

/* intro */
.intro{position:absolute;left:150px;top:620px;width:900px;text-align:center;font-size:11px;line-height:1.4;color:#555}
.intro p+p{margin-top:14px}

/* about */
.about{position:absolute;left:0;top:791px;width:1200px;height:471px;background:var(--grey-band)}
.about h2{position:absolute;left:117px;top:20px;font-size:30px;font-weight:700;color:var(--ink)}
.about h2 .hl{color:var(--red)}
.about-text{position:absolute;left:117px;top:62px;width:583px;font-size:10.6px;line-height:1.3;color:#555;text-align:justify}
.about-facts{position:absolute;left:117px;top:282px;width:530px;list-style:none}
.about-facts li{position:relative;padding-left:22px;color:var(--red);font-size:12px;line-height:1.75;margin-bottom:8px;text-align:justify}
.about-facts li::before{content:"";position:absolute;left:0;top:5px;width:11px;height:11px;border-radius:50%;background:var(--red)}
.about-facts li::after{content:"";position:absolute;left:3px;top:8px;width:4px;height:2px;border-left:1.5px solid #fff;border-bottom:1.5px solid #fff;transform:rotate(-45deg)}
.about-photo{position:absolute;left:723px;top:68px;width:369px;height:380px;background:linear-gradient(180deg,#d8d4cc 0%,#b9b2a6 45%,#4a5260 80%,#ececec 100%)}

/* practice */
.practice-intro{position:absolute;left:210px;top:1362px;width:780px;text-align:center;font-size:11px;line-height:1.4;color:#555}
.card{position:absolute;z-index:2;top:1436px;width:218px;height:246px;background:var(--card);padding:10px 14px;text-align:center}
.card h3{font-size:15px;font-weight:700;color:var(--ink);margin-bottom:12px}
.card p{font-size:10.6px;line-height:1.4;color:#666;text-align:justify}
.card.active{background:var(--red)}
.card.active h3,.card.active p{color:var(--white)}
.card-icon{position:absolute;left:50%;bottom:-20px;margin-left:-21px;width:42px;height:42px;border-radius:50%;background:var(--card);border:2px solid var(--white);box-shadow:0 2px 3px rgba(0,0,0,.2);display:flex;align-items:center;justify-content:center}
.card.active .card-icon{background:var(--red)}
.card:not(.active) .card-icon{background:#ededed}

/* stats */
.stats{position:absolute;z-index:1;left:0;top:1706px;width:1200px;height:270px;background:var(--stats-bg)}
.stat{position:absolute;top:30px;width:260px;text-align:center}
.stat svg{display:block;margin:0 auto}
.stat-value{position:absolute;left:0;width:260px;top:50px;font-size:20px;font-weight:700;color:var(--red)}
.stat-label{margin-top:22px;font-size:15px;font-weight:700;color:var(--red);line-height:1.5}

/* footer */
.site-footer{position:absolute;left:0;top:1976px;width:1200px;height:282px;background:var(--footer-bg);color:var(--footer-text)}
.site-footer h4{position:absolute;color:var(--red);font-size:15px;font-weight:700}
.contact-blurb{position:absolute;left:134px;top:52px;width:270px;font-size:11px;line-height:1.5}
.contact-list{position:absolute;left:134px;top:114px;list-style:none;font-size:11px;line-height:1.5}
.contact-list li{position:relative;padding-left:16px;margin-bottom:7px}
.contact-list svg{position:absolute;left:0;top:3px}
.quick-links{position:absolute;left:517px;top:54px;list-style:none;font-size:12px}
.quick-links li{position:relative;padding-left:23px;line-height:20.5px}
.quick-links li::before{content:"";position:absolute;left:3px;top:7px;width:7px;height:7px;border-radius:50%;background:var(--red)}
.newsletter-text{position:absolute;left:815px;top:58px;width:245px;font-size:12px;line-height:1.6;text-align:justify}
.newsletter-form{position:absolute;left:817px;top:128px;display:flex}
.newsletter-form .input{width:205px;height:36px;background:var(--white);color:#333;font-size:12px;display:flex;align-items:center;padding-left:12px}
.newsletter-form .go{width:34px;height:36px;background:var(--red);color:var(--white);font-size:12px;display:flex;align-items:center;justify-content:center}
.social{position:absolute;left:818px;top:189px;display:flex;gap:22px}
.social span{width:13px;height:13px;border-radius:50%;background:#777}
.copyright{position:absolute;left:805px;top:240px;font-size:9px}
</style>
</head>
<body>

<header class="site-header">
  <div class="brand"><span class="brand-square"></span><span class="brand-name">WENDROW LAW</span></div>
  <div class="call-btn">
    <svg width="16" height="16" viewBox="0 0 24 24"><path fill="#fff" d="M6.6 10.8a15.1 15.1 0 0 0 6.6 6.6l2.2-2.2c.3-.3.7-.4 1-.2 1.1.4 2.3.6 3.6.6.6 0 1 .4 1 1V20c0 .6-.4 1-1 1A17 17 0 0 1 3 4c0-.6.4-1 1-1h3.5c.6 0 1 .4 1 1 0 1.3.2 2.5.6 3.6.1.3 0 .7-.2 1z"/></svg>
    <span><b>Call</b> 855-WENDROW</span>
  </div>
</header>

<section class="hero">
  <div class="hero-photo" role="img" aria-label="Portrait of a smiling woman in front of law library bookshelves"></div>
</section>

<nav class="main-nav">
  <a class="active">Home</a><a>The Firm</a><a>Practice Areas</a><a>News</a><a>FAQ</a><a>Contact</a>
  <span class="nav-search"><svg width="16" height="16" viewBox="0 0 24 24"><circle cx="10" cy="10" r="6.5" fill="none" stroke="#fff" stroke-width="3"/><path d="M15 15l6 6" stroke="#fff" stroke-width="3"/></svg></span>
</nav>
<div class="slider-dots"><span></span><span></span><span></span><span></span></div>

<aside class="consult-card">
  <h2>Telephone harassment is a serious violation of your rights.</h2>
  <p class="lead">Carl Wendrow is a consumer lawyer dedicated to representing victims of telephone harassment and debt collector abuse. Have you been harassed? Don't delay, contact us today.</p>
  <div class="consult-form">
    <div class="field">Enter your telephone number</div>
    <div class="field-row"><div class="field">First name</div><div class="field">Last name</div></div>
    <div class="consult-btn"><span>Get your <b>FREE</b> Consultation</span></div>
  </div>
  <p class="note"><b>*We hate spam</b> and will never share your info with anyone else - guaranteed.</p>
</aside>

<h2 class="section-title" style="top:548px"><span class="hl">WENDROW LAW</span></h2>
<div class="title-rule" style="top:591px"></div>
<div class="intro">
  <p>Wendrow Law is a leading consumer protection law firm dedicated to protecting individuals from abuse by telemarketers, debt collectors, and large companies that abuse their power. Carl Wendrow, Esq. has recovered millions of dollars for aggrieved consumers all over the country.</p>
  <p>We have recovered over $25 million dollars for consumers, and we have individually represented more than 15,000 clients in Florida alone.</p>
  <p>At Wendrow Law, we are proud of the fact that we do not represent insurance companies, hospitals, or any large corporations. Our practice is strictly limited to representing consumers. Individuals. Human beings. If you have a problem, please reach out to us for a friendly consultation.</p>
</div>
<div class="btn-red" style="left:553px;top:742px;width:93px;height:30px">READ MORE</div>

<section class="about">
  <h2><span class="hl">ABOUT</span> CARL WENDROW</h2>
  <div class="about-text">
    <p>Carl Wendrow, Esq. focuses on all types of privacy and consumer protection litigation at both the state and federal level. We are not a credit repair or "debt consolidation" service; we are an aggressive litigation law firm that brings violators to justice in court.</p>
    <p>Carl Wendrow, Esq. has been representing consumers since 2006 in matters ranging from simple traffic tickets to complex privacy rights litigation. The firm concentrates on debt collector abuse, including telephone harassment, and other violations of federal consumer protection laws. Carl Wendrow is passionate about helping victims of harassment, and bringing predatory debt collectors to justice in court. Since 2009, Mr. Wendrow has advocated against invasive government surveillance programs involving photo-enforced traffic laws, and in 2010, he successfully obtained a trial court order holding that the City of Bayview's red-light camera program was unlawful. Additionally, Mr. Wendrow has been involved in several high-profile lawsuits regarding telemarketing abuses under the Telephone Consumer Protection Act.</p>
    <p>Carl Wendrow's practice focuses on violations of federal law committed by debt collectors, telemarketers, and spammers. If you have been the victim of debt collector harassment, abusive telemarketing, or cellular telephone spam, contact us for a free consultation.</p>
  </div>
  <ul class="about-facts">
    <li>Carl Wendrow, Esq. is a native Floridian, originally from Miami, Florida.</li>
    <li>Mr. Wendrow graduated summa cum laude from Coastal State University Law School in 2006.</li>
    <li>Mr. Wendrow obtained his bachelor's degree in Computer Science from Eastbrook University in Eastbrook, Maryland.</li>
  </ul>
  <div class="btn-red" style="left:117px;top:418px;width:93px;height:30px">READ MORE</div>
  <div class="about-photo" role="img" aria-label="Portrait of the attorney in a grey suit in front of framed diplomas and a plaque"></div>
</section>

<h2 class="section-title" style="top:1283px"><span class="hl">PRACTICE</span> AREAS</h2>
<div class="title-rule" style="top:1327px"></div>
<p class="practice-intro">Carl Wendrow, Esq. focuses on all types of consumer protection litigation at both the state and federal level. We are not a credit repair or "debt consolidation" service; we are an aggressive litigation law firm that brings violators to justice in court.</p>

<section class="stats">
  <div class="stat" style="left:173px">
    <svg width="120" height="120" viewBox="0 0 120 120"><circle cx="60" cy="60" r="50" fill="none" stroke="#2a2a2a" stroke-width="9"/><circle cx="60" cy="60" r="50" fill="none" stroke="var(--red)" stroke-width="9" stroke-dasharray="125.7 314.2" transform="rotate(90 60 60)"/></svg>
    <div class="stat-value">40 %</div>
    <div class="stat-label">X DOLLARS RECOVERED<br>CONSUMERS</div>
  </div>
  <div class="stat" style="left:469px">
    <svg width="120" height="120" viewBox="0 0 120 120"><circle cx="60" cy="60" r="50" fill="none" stroke="#2a2a2a" stroke-width="9"/><circle cx="60" cy="60" r="50" fill="none" stroke="var(--red)" stroke-width="9" stroke-dasharray="188.5 314.2" transform="rotate(-90 60 60)"/></svg>
    <div class="stat-value">60 %</div>
    <div class="stat-label">Y CLIENTS</div>
  </div>
  <div class="stat" style="left:751px">
    <svg width="120" height="120" viewBox="0 0 120 120"><circle cx="60" cy="60" r="50" fill="none" stroke="#2a2a2a" stroke-width="9"/><circle cx="60" cy="60" r="50" fill="none" stroke="var(--red)" stroke-width="9" stroke-dasharray="251.3 314.2" transform="rotate(-90 60 60)"/></svg>
    <div class="stat-value">80 %</div>
    <div class="stat-label">Z LAWSUITS FILED<br>CONSUMERS</div>
  </div>
</section>

<article class="card active" style="left:116px">
  <h3>Telephone Harassment</h3>
  <p>Carl Wendrow sues debt collectors, telemarketers, and spammers who violate the Telephone Consumer Protection Act ("TCPA"). Under the TCPA, violators can be held accountable and forced to pay heavy penalties to their victims. If you have been the subject of constant or abusive telephone calls, contact us for a free consultation.</p>
  <span class="card-icon"><svg width="16" height="16" viewBox="0 0 24 24"><path fill="#fff" d="M6.6 10.8a15.1 15.1 0 0 0 6.6 6.6l2.2-2.2c.3-.3.7-.4 1-.2 1.1.4 2.3.6 3.6.6.6 0 1 .4 1 1V20c0 .6-.4 1-1 1A17 17 0 0 1 3 4c0-.6.4-1 1-1h3.5c.6 0 1 .4 1 1 0 1.3.2 2.5.6 3.6.1.3 0 .7-.2 1z"/></svg></span>
</article>
<article class="card" style="left:366px">
  <h3>Text Message Spam</h3>
  <p>These days, advertisers are hard at work dreaming up new ways to get their brands in front of your eyes. It is becoming ever more common for unscrupulous companies to abuse your cellular telephone with so-called "text spam." These companies frequently violate federal law. When they cross the line, Carl Wendrow sues them and holds them accountable.</p>
  <span class="card-icon"><svg width="18" height="14" viewBox="0 0 18 14"><rect x="0" y="0" width="18" height="14" rx="1" fill="#666"/><path d="M1 1l8 7 8-7" fill="none" stroke="#ededed" stroke-width="1.5"/></svg></span>
</article>
<article class="card" style="left:616px">
  <h3>Consumer Protection</h3>
  <p>Debt collectors are in the business of coercing consumers to pay money without regard for their legal rights. They call day and night, send letters, annoy, threaten, and abuse. Often times their practices are prohibited by federal or state law. Carl Wendrow is versed in the law of unlawful debt collection practices, and holds offenders accountable in court. Contact us for a free consultation.</p>
  <span class="card-icon"><svg width="14" height="16" viewBox="0 0 14 16"><path d="M3.5 7V5a3.5 3.5 0 0 1 7 0v2" fill="none" stroke="#666" stroke-width="2"/><rect x="1" y="7" width="12" height="9" rx="1" fill="#666"/></svg></span>
</article>
<article class="card" style="left:866px">
  <h3>Privacy</h3>
  <p>The law of privacy is relatively new and rapidly evolving. With the advent of the Internet, new privacy concerns emerge on an almost-daily basis. If you believe your privacy rights have been violated, contact us for a free consultation.</p>
  <span class="card-icon"><svg width="20" height="12" viewBox="0 0 20 12"><path d="M1 6Q10-4 19 6Q10 16 1 6z" fill="#666"/><circle cx="10" cy="6" r="3" fill="#ededed"/><circle cx="10" cy="6" r="1.5" fill="#666"/></svg></span>
</article>

<footer class="site-footer">
  <h4 style="left:134px;top:18px">CONTACT US</h4>
  <p class="contact-blurb">Have a case you would like to discuss with us? Please feel free to call, email, or visit our office for a free consultation.</p>
  <ul class="contact-list">
    <li><svg width="9" height="12" viewBox="0 0 9 12"><path d="M4.5 0A4.5 4.5 0 0 0 0 4.5C0 8 4.5 12 4.5 12S9 8 9 4.5A4.5 4.5 0 0 0 4.5 0z" fill="var(--red)"/><circle cx="4.5" cy="4.5" r="1.6" fill="#0b0b0b"/></svg>Law Office of Carl Wendrow, Esq.<br>4100 Harbor Blvd., Ste 210<br>Bayview, FL 33100</li>
    <li><svg width="10" height="10" viewBox="0 0 24 24"><path fill="var(--red)" d="M6.6 10.8a15.1 15.1 0 0 0 6.6 6.6l2.2-2.2c.3-.3.7-.4 1-.2 1.1.4 2.3.6 3.6.6.6 0 1 .4 1 1V20c0 .6-.4 1-1 1A17 17 0 0 1 3 4c0-.6.4-1 1-1h3.5c.6 0 1 .4 1 1 0 1.3.2 2.5.6 3.6.1.3 0 .7-.2 1z"/></svg>1.855.555.0146</li>
    <li><svg width="10" height="10" viewBox="0 0 24 24"><path fill="var(--red)" d="M6.6 10.8a15.1 15.1 0 0 0 6.6 6.6l2.2-2.2c.3-.3.7-.4 1-.2 1.1.4 2.3.6 3.6.6.6 0 1 .4 1 1V20c0 .6-.4 1-1 1A17 17 0 0 1 3 4c0-.6.4-1 1-1h3.5c.6 0 1 .4 1 1 0 1.3.2 2.5.6 3.6.1.3 0 .7-.2 1z"/></svg>1.954.555.0141</li>
    <li><svg width="10" height="10" viewBox="0 0 10 10"><rect x="0" y="3" width="10" height="6" fill="var(--red)"/><rect x="2" y="0" width="6" height="3" fill="var(--red)"/></svg>1.954.555.0144</li>
    <li><svg width="10" height="8" viewBox="0 0 10 8"><rect width="10" height="8" fill="var(--red)"/><path d="M0 0l5 4 5-4" fill="none" stroke="#0b0b0b"/></svg>info@wendrowlaw.example</li>
  </ul>

  <h4 style="left:517px;top:18px">QUICK LINKS</h4>
  <ul class="quick-links">
    <li>Home</li><li>The Firm</li><li>Practice Areas</li><li>News</li><li>FAQ</li><li>Contact</li>
  </ul>

  <h4 style="left:815px;top:24px">NEWSLETTER</h4>
  <p class="newsletter-text">Nulla facilisi. Vivamus lacus libero, ultrices non ullamcorper ac, tempus sit amet enim. Suspendisse at semper ipsum.</p>
  <div class="newsletter-form"><div class="input">Enter email id</div><div class="go">GO</div></div>
  <div class="social"><span></span><span></span><span></span><span></span></div>
  <p class="copyright">© 2016 • www.wendrowlaw.example • PRIVACY POLICY</p>
</footer>

</body>
</html>
```